Simple, Professional and neat business card design for Vendralo Inc.

We're looking to re-vamp our business card design. We're a supplier of innovative feed ingredients for the North American animal agriculture industry. We are located in Lucknow, Ontario, Canada and our flagship product is a product that prevents milk fever in dairy cows when the calve, it is fed before calving and is very effective compared to other alternatives available on the market today.

Our company has Danish roots and we import all of our product from our Danish partner/manufacturer in Denmark. We like our design to embrace high professionalism while remaining neat and simple.

Target Market(s)

B2B, Feed Mills, Veterinary Clinics, Large integrators/producers,

Industry/Entity Type

Agribusiness

Contact Information for Business Card

We like the rounded corners because they make the card easy to sit in a wallet and not many use it so it makes the card stand out, just possibly something to take account for during the design.

As you can also see on the sliders below, looking for a that simple but proffesional scandinavian design.

Requirements
Nice to have
• Rounded corners
Should not have
• Too vibrant

```html
<!DOCTYPE html>
<html lang="en">
<head>
<meta charset="utf-8">
<title>Vendralo Inc. Business Card</title>
<link rel="stylesheet" href="https://fonts.googleapis.com/css2?family=Open+Sans:wght@400;600;700&display=swap">
<style>
  :root {
    --brand-blue: #1a5cad;
    --brand-blue-dark: #154d93;
    --card-white: #f4f5f7;
    --ink: #1e1e1e;
    --accent-sand: #c9b98a;
    --page-bg: #2b2b2b;
    --rule-light: rgba(255,255,255,0.35);
  }
  * { box-sizing: border-box; margin: 0; padding: 0; }
  html, body { width: 1200px; height: 997px; overflow: hidden; }
  body {
    background: var(--page-bg);
    font-family: "Open Sans", Arial, sans-serif;
    position: relative;
  }
  .card {
    position: absolute;
    left: 250px;
    width: 700px;
    height: 400px;
    border-radius: 26px;
    overflow: hidden;
    background: var(--card-white);
    box-shadow: 0 10px 30px rgba(0,0,0,0.5);
  }
  /* ---------- Back ---------- */
  .card-back { top: 60px; }
  .back-header {
    height: 100px;
    display: flex;
    align-items: center;
    padding-left: 60px;
    gap: 18px;
  }
  .brand-dot {
    width: 46px; height: 46px; border-radius: 50%;
    background: var(--accent-sand);
  }
  .back-name {
    font-size: 38px; font-weight: 700; color: var(--brand-blue);
    letter-spacing: 0.5px;
  }
  .back-body {
    background: var(--brand-blue);
    height: 300px;
    padding: 24px 60px 0;
    color: #fff;
  }
  .back-intro { font-size: 18px; font-weight: 600; line-height: 1.4; max-width: 470px; }
  .benefits {
    display: flex; margin-top: 34px;
  }
  .benefit {
    flex: 1; display: flex; flex-direction: column; align-items: center; gap: 12px;
    border-right: 1px solid var(--rule-light);
  }
  .benefit:last-child { border-right: none; }
  .benefit svg { width: 66px; height: 66px; }
  .benefit-label { font-size: 14px; }
  /* ---------- Front ---------- */
  .card-front { top: 527px; display: flex; }
  .front-brand {
    width: 420px; background: var(--brand-blue); color: #fff;
    display: flex; flex-direction: column; align-items: center; justify-content: center;
    padding: 0 30px;
  }
  .front-dot {
    width: 96px; height: 96px; border-radius: 50%;
    background: var(--accent-sand); margin-bottom: 22px;
  }
  .front-name { font-size: 36px; font-weight: 700; letter-spacing: 0.5px; }
  .front-tagline { font-size: 21px; margin-top: 6px; }
  .front-tollfree { font-size: 20px; font-weight: 600; margin-top: 26px; }
  .front-contact {
    flex: 1; padding: 46px 34px 0 20px;
    display: flex; flex-direction: column; align-items: flex-end; gap: 30px;
    text-align: right;
  }
  .contact-group {
    border-right: 2px solid var(--brand-blue);
    padding-right: 10px;
  }
  .person-name { font-size: 17px; font-weight: 700; color: var(--brand-blue); letter-spacing: 0.5px; }
  .person-role { font-size: 12px; color: var(--ink); }
  .address { font-size: 15px; color: var(--brand-blue); line-height: 1.4; }
  .lines { font-size: 15px; color: var(--ink); line-height: 1.5; }
  .web { color: var(--brand-blue); font-weight: 700; }
</style>
</head>
<body>

<section class="card card-back">
  <header class="back-header">
    <span class="brand-dot"></span>
    <span class="back-name">VENDRALO INC.</span>
  </header>
  <div class="back-body">
    <p class="back-intro">Distributor of innovative feed ingredients and other preventative health products.</p>
    <div class="benefits">
      <div class="benefit">
        <svg viewBox="0 0 66 66" aria-hidden="true">
          <path d="M33 6 L56 14 V32 C56 46 46 56 33 61 C20 56 10 46 10 32 V14 Z" fill="none" stroke="#fff" stroke-width="3"/>
          <circle cx="33" cy="32" r="10" fill="#fff"/>
          <path d="M33 26 V38 M27 32 H39" stroke="var(--brand-blue)" stroke-width="3"/>
        </svg>
        <span class="benefit-label">Preventative Care</span>
      </div>
      <div class="benefit">
        <svg viewBox="0 0 66 66" aria-hidden="true">
          <circle cx="33" cy="33" r="26" fill="none" stroke="#fff" stroke-width="3" stroke-dasharray="4 4"/>
          <path d="M18 44 L28 34 L36 40 L50 22" fill="none" stroke="#fff" stroke-width="3.5"/>
          <path d="M42 22 H50 V30" fill="none" stroke="#fff" stroke-width="3.5"/>
        </svg>
        <span class="benefit-label">High-performance</span>
      </div>
      <div class="benefit">
        <svg viewBox="0 0 66 66" aria-hidden="true">
          <circle cx="33" cy="33" r="26" fill="none" stroke="#fff" stroke-width="3"/>
          <rect x="22" y="24" width="22" height="18" rx="3" fill="#fff"/>
          <path d="M15 51 L51 15" stroke="#fff" stroke-width="4"/>
        </svg>
        <span class="benefit-label">Prescription-free</span>
      </div>
    </div>
  </div>
</section>

<section class="card card-front">
  <div class="front-brand">
    <span class="front-dot"></span>
    <h1 class="front-name">VENDRALO INC.</h1>
    <p class="front-tagline">Protecting the health of your animals</p>
    <p class="front-tollfree">Toll-Free 888-555-0135</p>
  </div>
  <div class="front-contact">
    <div class="contact-group">
      <p class="person-name">MIKKEL SORENSEN</p>
      <p class="person-role">Managing Director</p>
    </div>
    <div class="contact-group address">
      <p>Box 42, Westbrook, Ontario Canada</p>
      <p>N0X 1A0</p>
    </div>
    <div class="contact-group lines">
      <p>555-010-0333</p>
      <p>555-010-5822</p>
      <p>555-010-5999</p>
      <p>mikkel@vendralo.com</p>
      <p class="web">www.vendralo.com</p>
    </div>
  </div>
</section>

</body>
</html>
```